Dentist Seminar invite please see .doc in attachments

Need an 8.5 x 11 invite designed. It will be for an invitation to attend an evening seminar on dental procedures. Feel free to utilize both front and back ONLY IF REQUIRED

See Assets & PPT with additional assets.

INSPIRATION: FIle NAME KOLVEN

Target Market(s)

Dentists

Industry/Entity Type

Dental

Other font styles liked:
• lato, garamond, palatino linotype

Colors
cee9f5
9bcb3c
0492cd
cadf82

Requirements
Must have
• Must have the colours suggested, and professional feel.
• Some of the assets merged cleanly into the design
Should not have
• Any pictures of teeth, tooth brushes or any dental product

```html
<!DOCTYPE html>
<html lang="en">
<head>
<meta charset="utf-8">
<title>Evening Seminar on Dental Procedures</title>
<link rel="stylesheet" href="https://fonts.googleapis.com/css2?family=Source+Sans+3:wght@300;400;600;700&display=swap">
<style>
  :root {
    --blue: #0a93cf;
    --green: #9bcb3c;
    --charcoal: #555759;
    --charcoal-line: #6a6c6e;
    --panel-grey: #e6e7e8;
    --ink: #3a3a3c;
    --muted: #6d6e71;
    --white: #ffffff;
  }
  * { box-sizing: border-box; margin: 0; padding: 0; }
  html, body { width: 1000px; height: 1200px; overflow: hidden; background: #fff; }
  body { font-family: "Source Sans 3", "Myriad Pro", sans-serif; color: var(--ink); }
  .invite { position: relative; width: 1000px; height: 1200px; background: var(--white); overflow: hidden; }

  .header-shapes { position: absolute; left: 0; top: 0; }
  .title-block { position: absolute; left: 62px; top: 84px; color: var(--white); }
  .title-kicker { font-size: 27px; font-weight: 400; line-height: 1; }
  .title-main { font-size: 41px; font-weight: 700; line-height: 1; margin-top: 10px; white-space: nowrap; }
  .event-date { position: absolute; left: 61px; top: 232px; color: var(--white); font-size: 25px; font-weight: 400; }

  .tablet { position: absolute; border-radius: 12px; background: linear-gradient(135deg, #1d1d1f 0%, #3c3c3f 50%, #9fa1a4 100%); }
  .tablet-front { left: 532px; top: 39px; width: 214px; height: 259px; }
  .tablet-back { left: 752px; top: 98px; width: 230px; height: 200px; }
  .software-name { position: absolute; left: 760px; top: 60px; font-size: 23px; font-weight: 300; color: var(--ink); white-space: nowrap; }
  .software-name small { font-size: 11px; color: var(--muted); margin-left: 4px; vertical-align: top; }
  .software-caption { position: absolute; left: 694px; top: 320px; font-size: 14px; font-weight: 300; color: var(--muted); }

  .clinical-photo { position: absolute; left: 61px; top: 364px; width: 192px; height: 118px;
    background: linear-gradient(180deg, #8e2a2c 0%, #c9575a 55%, #e8c8b8 100%); }
  .guide-model { position: absolute; left: 61px; top: 520px; width: 192px; height: 124px;
    background: radial-gradient(ellipse at 50% 40%, #8a2f7f 0%, #8fcf9c 55%, #f3f1ea 100%); border-radius: 40% 40% 30% 30%; }
  .overview { position: absolute; left: 281px; top: 365px; width: 697px; font-size: 17px; line-height: 21.3px; text-align: justify; color: var(--ink); }
  .overview p + p { margin-top: 21px; }

  .objectives { position: absolute; left: 0; top: 679px; width: 1000px; height: 233px; background: var(--blue); }
  .objectives-tab { position: absolute; left: 0; top: 10px; }
  .objectives-title { position: absolute; left: 61px; top: 14px; color: var(--white); font-size: 22px; font-weight: 400; }
  .objectives-list { position: absolute; left: 58px; top: 72px; list-style: none; color: var(--white); font-size: 17.4px; line-height: 21.3px; letter-spacing: -0.3px; white-space: nowrap; }
  .objectives-list li::before { content: "\2022"; margin-right: 3px; }
  .jaw-model { position: absolute; left: 770px; top: 652px; width: 200px; height: 150px;
    background: linear-gradient(160deg, #d9dadc 0%, #b8babd 60%, #f2b45a 100%); border-radius: 30% 20% 40% 30%; }
  .notch-down { position: absolute; left: 478px; top: 911px; }

  .presenter { position: absolute; left: 0; top: 912px; width: 1000px; height: 228px; background: var(--panel-grey); }
  .presenter-photo { position: absolute; left: 60px; top: 34px; width: 174px; height: 174px; border-radius: 50%;
    border: 3px solid var(--white); background: radial-gradient(circle at 50% 40%, #c9c3bd 0%, #9a9591 60%, #5b5a5c 100%); }
  .presenter-name { position: absolute; left: 279px; top: 42px; font-size: 17px; font-weight: 400; color: #1e1e20; letter-spacing: -0.2px; white-space: nowrap; }
  .presenter-bio { position: absolute; left: 279px; top: 71px; width: 697px; font-size: 14.6px; line-height: 18.3px; text-align: justify; color: var(--muted); letter-spacing: -0.2px; }

  .footer { position: absolute; left: 0; top: 1140px; width: 1000px; height: 60px; background: var(--charcoal); color: var(--white); }
  .notch-up { position: absolute; left: 478px; top: -20px; }
  .venue { position: absolute; left: 100px; top: 12px; font-size: 14.5px; line-height: 18px; }
  .registration { position: absolute; left: 657px; top: 8px; font-size: 17px; line-height: 21px; }
  .icon { position: absolute; }
</style>
</head>
<body>
<main class="invite">

  <svg class="header-shapes" width="1000" height="340" viewBox="0 0 1000 340" aria-hidden="true">
    <polygon points="0,0 686,0 364,335 0,335" fill="var(--charcoal)"/>
    <polyline points="0,290 420,290 456,253" fill="none" stroke="var(--charcoal-line)" stroke-width="1.5"/>
    <rect x="0" y="74" width="532" height="126" fill="var(--blue)"/>
    <polygon points="0,218 522,218 463,277 0,277" fill="var(--green)"/>
  </svg>

  <header class="title-block">
    <p class="title-kicker">EVENING SEMINAR ON</p>
    <h1 class="title-main">DENTAL PROCEDURES</h1>
  </header>
  <p class="event-date">November 13, 2017&nbsp; 6:30 – 9:30pm</p>

  <div class="tablet tablet-front" role="img" aria-label="Tablet showing a 3D jaw scan with planned implants in the planning software"></div>
  <div class="tablet tablet-back" role="img" aria-label="Tablet showing CT scan views in the planning software"></div>
  <p class="software-name">PlanView<small>PRESENTER</small></p>
  <p class="software-caption">for Slate Tablet</p>

  <div class="clinical-photo" role="img" aria-label="Clinical photo of an implant placed between front teeth"></div>
  <div class="guide-model" role="img" aria-label="3D rendering of a printed surgical guide with implant drill paths"></div>

  <section class="overview">
    <p>This presentation will cover the recent advances in digital technology and its use in dentistry.&nbsp; Digital protocols will be introduced that can improve upon traditional treatment planning approaches.&nbsp; The use of modern 3D technology and the digital workflow can simplify advanced procedures enhancing the predictability of the surgical outcomes. Through the use of state of the art diagnostic imaging technologies, intra-oral scanning, live guided navigation,&nbsp; and 3D printing; multiple digital workflows and their surgical applications will be discussed through real clinical cases from Dr Arvane's surgical practice.</p>
    <p>This groundbreaking lecture will showcase the synergy between advanced technology and fundamental biological principles to revolutionize the modern practice of periodontics and implantology.&nbsp; Multiple innovative protocols to treat advanced surgical cases will be presented with techniques that have never been seen before.</p>
  </section>

  <section class="objectives">
    <svg class="objectives-tab" width="370" height="40" viewBox="0 0 370 40" aria-hidden="true">
      <polygon points="0,0 362,0 325,40 0,40" fill="var(--green)"/>
    </svg>
    <h2 class="objectives-title">Learning Objectives:</h2>
    <ul class="objectives-list">
      <li>Discuss the use of modern digital technologies like CBCT, intra-oral scanning, and 3D printing.</li>
      <li>Learn to digitally plan surgical procedures and use 3D printed surgical guides</li>
      <li>Understand the benefits of microsurgery and the use of surgical operating microscope</li>
      <li>Understand the benefits of digital technology in surgical treatment planning</li>
      <li>Understanding and benefits of live guided navigation surgery and its applications</li>
      <li>Learn about innovative procedures like digitally guided bone block harvesting, digitally created bone grafts, &amp; osteotomy guides.</li>
      <li>Understand how computer automated design software can improve upon real live surgery.</li>
    </ul>
  </section>
  <div class="jaw-model" role="img" aria-label="3D model of a lower jaw with colour-coded planned implants"></div>

  <section class="presenter">
    <div class="presenter-photo" role="img" aria-label="Portrait photo of the presenter"></div>
    <h3 class="presenter-name">DR. KOLVEN ARVANE Hon B.Sc., D.M.D., M.S.D., Dip. Perio., F.R.C.D.(C)</h3>
    <p class="presenter-bio">Dr. Kolven Arvane received his Honours Bachelor of Science degree from the University of Lakeshore. After a year of periodontal research at Harbourview Hospital, he attended dental school at Eastbridge University and completed his Doctor of Dental Medicine degree. Graduating from dental school with magna cum laude and the North American Society of Periodontics Student of the Year Award for achievement in Periodontics, Dr. Arvane further pursued his studies at Westfield Reserve University in Ashford to complete his specialty training in Periodontics.</p>
  </section>
  <svg class="notch-down" width="44" height="26" viewBox="0 0 44 26" aria-hidden="true">
    <polygon points="0,0 44,0 22,24" fill="var(--blue)"/>
  </svg>

  <footer class="footer">
    <svg class="notch-up" width="44" height="22" viewBox="0 0 44 22" aria-hidden="true">
      <polygon points="0,22 22,0 44,22" fill="var(--charcoal)"/>
    </svg>
    <svg class="icon" style="left:56px;top:16px" width="18" height="26" viewBox="0 0 18 26" aria-hidden="true">
      <path d="M9 0C4 0 0 4 0 9c0 6.5 9 17 9 17s9-10.5 9-17C18 4 14 0 9 0zm0 12.5A3.5 3.5 0 1 1 9 5.5a3.5 3.5 0 0 1 0 7z" fill="var(--white)"/>
    </svg>
    <p class="venue">Maplegrove Banquet Hall 482 Orchard Ln.<br>Toronto, Ontario M0X 1A0</p>
    <svg class="icon" style="left:618px;top:17px" width="24" height="24" viewBox="0 0 24 24" aria-hidden="true">
      <path d="M6.6 10.8a15.1 15.1 0 0 0 6.6 6.6l2.2-2.2c.3-.3.7-.4 1-.2 1.1.4 2.3.6 3.6.6.6 0 1 .4 1 1V20c0 .6-.4 1-1 1A17 17 0 0 1 3 4c0-.6.4-1 1-1h3.5c.6 0 1 .4 1 1 0 1.3.2 2.5.6 3.6.1.3 0 .7-.2 1l-2.3 2.2z" fill="var(--white)"/>
    </svg>
    <p class="registration">Registration: events@example.com<br>555-014-2273</p>
  </footer>

</main>
</body>
</html>
```